Birchmoor Yard Care_2015 New Cards_V1

We need an enhanced business card from what we have today. We are a Landscaping company and we have an existing Logo and text info that we would like to include.
Text to include:
In business for over 20 years,Fully Insured, Weekly Lawn Maintenance, Spring & Fall Clean-up, Todd Pierson, 203-555-0147, www.birchmooryardcarect.example, Visit our Website for additional Lawn Care Services or email directly at TODD@BIRCHMOORYARDCARE.EXAMPLE, We appreciate your business.
We want full color background and we will want to take this design and work with a printer that does high graphic silk screen cards. The colors we have thought about are Black, with our Green Logo, with Gold Text...we are open to different colors, we just want the card to wow!

Target Market(s)

Lawn Care Maintenance

Industry/Entity Type

Lawn Care

Contact Information for Business Card

Text to include:
In business for over 20 years, Fully Insured, Weekly Lawn Maintenance, Spring & Fall Clean-up, Todd Pierson, 203-555-0147, www.birchmooryardcarect.example, Visit our Website for additional Lawn Care Services or email directly at TODD@BIRCHMOORYARDCARE.EXAMPLE, We appreciate your business.

Requirements
Must have
• Logo, text details about how to reach us, standard size business cards that go horizontal.
Nice to have
• background colors, background designs, raised embossed lettering, rounded corners(2 or 4),

```html
<!DOCTYPE html>
<html lang="en">
<head>
<meta charset="utf-8">
<title>Birchmoor Yard Care – Business Cards</title>
<link rel="stylesheet" href="https://fonts.googleapis.com/css2?family=Montserrat:wght@700;800&family=Open+Sans:wght@400;600&display=swap">
<style>
  :root {
    --page: #ecebe6;
    --forest: #1c5a2c;
    --forest-deep: #144522;
    --paper: #f7f7f5;
    --lime: #8cc63f;
    --grass: #3f9a2e;
    --grass-deep: #1f7a27;
    --white: #ffffff;
  }
  * { margin: 0; padding: 0; box-sizing: border-box; }
  html, body { width: 1200px; height: 780px; overflow: hidden; }
  body {
    background: var(--page);
    display: flex;
    align-items: center;
    justify-content: center;
    gap: 50px;
    font-family: "Open Sans", Arial, sans-serif;
  }
  .card {
    position: relative;
    width: 540px;
    height: 309px;
    border-radius: 16px;
    overflow: hidden;
    box-shadow: 0 6px 18px rgba(0,0,0,.18);
  }

  /* Front */
  .card-front { background: var(--paper); }
  .front-brand {
    height: 190px;
    display: flex;
    flex-direction: column;
    align-items: center;
    justify-content: center;
    gap: 14px;
  }
  .wordmark {
    display: flex;
    align-items: center;
    gap: 12px;
    font-family: "Montserrat", Arial, sans-serif;
    font-weight: 800;
    font-size: 34px;
    color: var(--forest);
    letter-spacing: .5px;
  }
  .wordmark-dot {
    width: 22px; height: 22px; border-radius: 50%;
    background: var(--forest);
  }
  .tagline-spaced {
    font-family: "Montserrat", Arial, sans-serif;
    font-weight: 700;
    font-size: 13px;
    letter-spacing: 7px;
    color: var(--forest);
    text-transform: uppercase;
  }
  .front-band {
    position: absolute;
    left: 0; right: 0; bottom: 0;
    height: 119px;
    background: linear-gradient(180deg, var(--forest), var(--forest-deep));
    display: flex;
    align-items: center;
    padding: 0 34px;
    color: var(--white);
  }
  .contact-name {
    font-family: "Montserrat", Arial, sans-serif;
    font-weight: 700;
    font-size: 24px;
    width: 190px;
  }
  .band-divider {
    width: 1px; height: 66px;
    background: rgba(255,255,255,.7);
    margin: 0 18px 0 6px;
  }
  .contact-list { list-style: none; display: flex; flex-direction: column; gap: 5px; }
  .contact-item { display: flex; align-items: center; gap: 8px; font-size: 13px; }
  .contact-icon {
    width: 16px; height: 16px; border-radius: 3px;
    background: var(--white);
    display: flex; align-items: center; justify-content: center;
    flex: none;
  }

  /* Back */
  .card-back {
    background: radial-gradient(circle at 25% 25%, var(--lime) 0%, var(--grass) 45%, var(--grass-deep) 100%);
    color: var(--white);
  }
  .back-texture { position: absolute; inset: 0; }
  .back-content {
    position: relative;
    height: 100%;
    display: flex;
    flex-direction: column;
    align-items: center;
    padding-top: 62px;
  }
  .back-content .wordmark { color: var(--white); font-size: 40px; }
  .back-content .wordmark-dot { background: var(--white); }
  .back-content .tagline-spaced { color: var(--white); margin-top: 12px; font-size: 14px; }
  .service-list {
    margin-top: 34px;
    text-align: center;
    font-size: 13px;
    line-height: 1.55;
    font-weight: 600;
  }
</style>
</head>
<body>

<article class="card card-front">
  <div class="front-brand">
    <div class="wordmark"><span class="wordmark-dot"></span>Birchmoor Yard Care</div>
  </div>
  <div class="front-band">
    <p class="contact-name">Todd Pierson</p>
    <span class="band-divider"></span>
    <ul class="contact-list">
      <li class="contact-item">
        <span class="contact-icon">
          <svg width="10" height="10" viewBox="0 0 24 24"><path fill="#1c5a2c" d="M6.6 10.8a15 15 0 0 0 6.6 6.6l2.2-2.2a1 1 0 0 1 1-.25 11 11 0 0 0 3.6.6 1 1 0 0 1 1 1V20a1 1 0 0 1-1 1A17 17 0 0 1 3 4a1 1 0 0 1 1-1h3.5a1 1 0 0 1 1 1c0 1.25.2 2.45.6 3.6a1 1 0 0 1-.25 1z"/></svg>
        </span>203-555-0147
      </li>
      <li class="contact-item">
        <span class="contact-icon">
          <svg width="11" height="9" viewBox="0 0 24 18"><rect x="1" y="1" width="22" height="16" fill="none" stroke="#1c5a2c" stroke-width="2"/><path d="M1 1l11 9 11-9" fill="none" stroke="#1c5a2c" stroke-width="2"/></svg>
        </span>todd@birchmooryardcare.example
      </li>
      <li class="contact-item">
        <span class="contact-icon">
          <svg width="11" height="11" viewBox="0 0 24 24"><circle cx="12" cy="12" r="10" fill="none" stroke="#1c5a2c" stroke-width="2"/><path d="M2 12h20M12 2c3 3 3 17 0 20M12 2c-3 3-3 17 0 20" fill="none" stroke="#1c5a2c" stroke-width="2"/></svg>
        </span>www.birchmooryardcarect.example
      </li>
    </ul>
  </div>
</article>

<article class="card card-back">
  <div class="back-texture" role="img" aria-label="Textured grass background in bright and deep greens"></div>
  <div class="back-content">
    <div class="wordmark"><span class="wordmark-dot"></span>Birchmoor Yard Care</div>
    <ul class="service-list">
      <li>Weekly Mowing | Spring &amp; Fall Clean-Ups | Mulching of Flower/Plant Beds</li>
      <li>Edging | Hedge &amp; Shrub Trimming | Tree &amp; Shrub Plantings</li>
      <li>Light Tree Trimming</li>
    </ul>
  </div>
</article>

</body>
</html>
```